Creation of a cover for a book with an image provided. It is mainly a typographical work. PICTURE (Quiet Harbor IV) IS NOW AVAILABLE

Target Market(s)

General Public

Colors

Designer to choose colors to be used in the design.

Requirements
Must have
• Upper edge: "Mireille Fontaz" (author) Title: "Rain before the harvest" Bottom edge: "Marrow Editions"

```html
<!DOCTYPE html>
<html lang="en">
<head>
<meta charset="utf-8">
<title>Rain before the harvest — Mireille Fontaz</title>
<link rel="stylesheet" href="https://fonts.googleapis.com/css2?family=Cormorant+Garamond:wght@400;500&display=swap">
<style>
  :root {
    --backdrop: #e4e4e4;
    --ink-night: #0b0a0a;
    --ink-deep: #181312;
    --ink-warm: #2a1c17;
    --smoke-grey: #3e3d42;
    --type-white: #f4f1ec;
  }
  * { margin: 0; padding: 0; box-sizing: border-box; }
  html, body {
    width: 1200px;
    height: 745px;
    overflow: hidden;
    background: var(--backdrop);
  }
  .stage {
    position: relative;
    width: 1200px;
    height: 745px;
  }
  .cover {
    position: absolute;
    left: 390px;
    top: 28px;
    width: 420px;
    height: 689px;
    background: var(--ink-night);
    overflow: hidden;
    font-family: "Cormorant Garamond", "Garamond", serif;
    color: var(--type-white);
  }
  .cover-artwork {
    position: absolute;
    inset: 0;
    background:
      linear-gradient(100deg, var(--ink-night) 0%, var(--ink-warm) 45%, var(--ink-deep) 75%, var(--smoke-grey) 100%);
    opacity: 0.9;
  }
  .cover-author {
    position: absolute;
    top: 38px;
    left: 0;
    right: 0;
    text-align: center;
    font-weight: 400;
    font-size: 26px;
    letter-spacing: 0.12em;
    text-transform: uppercase;
  }
  .cover-title {
    position: absolute;
    top: 300px;
    left: 40px;
    right: 0;
    text-align: center;
    font-weight: 400;
    font-size: 80px;
    line-height: 0.9;
  }
  .cover-title span { display: block; }
  .cover-publisher {
    position: absolute;
    bottom: 34px;
    left: 0;
    right: 0;
    text-align: center;
    font-weight: 500;
    font-size: 14px;
    letter-spacing: 0.1em;
    text-transform: uppercase;
  }
</style>
</head>
<body>
  <main class="stage">
    <article class="cover">
      <div class="cover-artwork" role="img" aria-label="Cover artwork in dark warm tones"></div>
      <p class="cover-author">Mireille Fontaz</p>
      <h1 class="cover-title">
        <span>Rain</span>
        <span>before</span>
        <span>the</span>
        <span>harvest</span>
      </h1>
      <p class="cover-publisher">Marrow Editions</p>
    </article>
  </main>
</body>
</html>
```